Vantor Grid Advisory Partners - Website

Design & Build a website for a new company which operates in the Systems and Technology space for Transportation, Government and Commercial sectors.

Overall design should be minimalist in nature.
Should also have a feed that provides news and event updates on the main page.
Logo has already been awarded and should be incorporated into the site.

We like the overall layout, functionality and simplicity of the below sites. Submitted designs could be similar to or a combination of the aspects on these sites, or perhaps a whole different concept - we are open to new ideas.
Morqeli.com
Tumb.it

All I am moving away from the Tumb.it website and would like it to be more aligned with Morqeli.com not only in layout but in functionality. I will be extending the deadline of this design brief for two weeks to incorporate additional requirements and will add addtional funding to the project.

Apologies for not having more information available to provide but with so many submissions its getting confusing.

Thanks Dorian

Important: We will need two language versions of the website, English and Arabic; the website is hosted on HostPivo

Hello All, Thank you for your submissions. We have narrowed it down to the final 6 designers and I just wanted to take a moment and provide a bit of feedback regarding the concepts that we like and the modifications we are looking for. First, let me mention some of the design functions we like. - At the top of the homepage we really like the "region" or "language" tab so that the website can be viewed in both English and Arabic. - We like the homepage to have clear color variation so that the different sections of the homepage are distinct. Additionally, we like the bottom portion of the homepage to be in red. We feel that draws attention to our contact information. Again, we would like the colors to integrate black, gray-scale, red, etc. - Having a search tab at the top of the home page, or integrated into the main image, so that the site is easy to navigate. - We especially like the main image to have the scrolling tabs at the bottom so it is easy to browse the services offered (Consultancy, Solutions Architecture, Masters Systems Integration, Independent Design Review). - In regards to the services offered tab we really like the idea that a few people presented that have the outside of our logo with an icon in the middle of consultancy, solutions, etc., etc. Secondly, as mentioned in our brief we really enjoy the design of morqeli site. Specially, we enjoy the strong iconic images they use, the way the tabs at the top scroll easily, and contact us page that generates an email. Lastly, I've included some photos of the concept we have been working on. What we are trying to demonstrate is how our company offers a range of services that are essentially linked together. We provide individual services that when combined present the full service package. We would like this concept to be integrated into the over concept of our website. Please feel free to ask for clarification of any of the above points or contact us if you have any additional questions. We appreciate all of your hard work and are very excited to see the updated designs. Best, Miriam Okaford Vangridex Senior Program Manager miriam.okaford@vangridax.example

Industry/Entity Type

Government

Font styles to use
Serif
Sans Serif

Requirements
Must have
• Must work on/adapt to various/mobile devices (responsive)
Must be simple and straightforward
Colors should be in line/matching with logo
2 language versions: English and Arabic (no Thai)
Services should be the first group/row of items after/below the main image
Note: the website will be hosted by hostpivo
Nice to have
• Submit feedback form
What's New section
The banner at the bottom of the site should not be too large; we would like a narrow one more
It would be nice if the header/top banner (with Home, About, etc. tabs) could stay in place as you scroll down (like Morqeli and Chatterly)
We will likely only use one image with a Company slogan on the Home page rather than a carousel of images to rotate through
Should not have
• This is the existing website: http://www.vangridex.example
We do not like the animation, the way the banner icons/titles bounce
Not simple enough, we don't like the functionality or how pages load so slowly
We do not like the logo centered - it should be at the left
The banner and its tabs should not be towards the right, we would like them to be centered, to go all the way across and to be below the logo

```html
<!DOCTYPE html>
<html lang="en">
<head>
<meta charset="utf-8">
<title>Vangridex International – Home</title>
<link rel="stylesheet" href="https://fonts.googleapis.com/css2?family=PT+Sans:wght@400;700&display=swap">
<style>
  :root {
    --red: #e11b22;
    --red-dark: #c8161d;
    --red-deep: #d41920;
    --text: #333333;
    --muted: #7a7a7a;
    --field: #eeeeee;
    --band: #f1f1f1;
    --white: #ffffff;
    --dark-box: rgba(30, 30, 30, 0.85);
  }
  * { margin: 0; padding: 0; box-sizing: border-box; }
  html, body { width: 739px; height: 1200px; overflow: hidden; }
  body {
    position: relative;
    font-family: "PT Sans", Arial, sans-serif;
    color: var(--text);
    background: var(--white);
  }
  .abs { position: absolute; }

  /* Header */
  .site-header { position: absolute; left: 0; top: 0; width: 739px; height: 98px; }
  .brand { left: 74px; top: 38px; display: flex; align-items: center; gap: 8px; }
  .brand-mark { width: 14px; height: 14px; background: var(--red); }
  .brand-name { color: var(--red); font-weight: 700; font-size: 17px; letter-spacing: 2px; }
  .social { left: 426px; top: 10px; display: flex; gap: 4px; }
  .social span { width: 19px; height: 19px; background: #8a8a8a; border-radius: 2px; display: block; }
  .call { left: 534px; top: 10px; color: var(--red); font-size: 15px; }
  .btn-signin { left: 554px; top: 46px; width: 42px; height: 19px; background: var(--red); color: var(--white); font-size: 10px; text-align: center; line-height: 19px; }
  .btn-register { left: 604px; top: 46px; width: 54px; height: 19px; background: #d9d9d9; color: #444; font-size: 10px; text-align: center; line-height: 19px; }

  /* Navigation */
  .main-nav { left: 0; top: 98px; width: 739px; height: 28px; background: linear-gradient(var(--red), var(--red-dark)); }
  .main-nav a { position: absolute; top: 6px; color: var(--white); font-size: 11.5px; text-decoration: none; }
  .search { left: 545px; top: 3px; width: 124px; height: 22px; background: var(--white); border-radius: 11px; font-size: 8px; color: #666; padding: 6px 0 0 11px; }
  .search svg { position: absolute; right: 9px; top: 4px; }

  /* Hero */
  .hero { left: 0; top: 126px; width: 739px; height: 308px; background: linear-gradient(180deg, #5f6f82 0%, #8e9bab 45%, #c9b6a6 80%, #dcc6b6 100%); }
  .hero-caption { left: 69px; top: 160px; width: 305px; height: 115px; background: var(--dark-box); color: var(--white); font-size: 16px; font-weight: 700; line-height: 20.5px; padding: 20px 0 0 16px; }
  .hero-dots { left: 610px; top: 266px; display: flex; gap: 5px; }
  .hero-dots span { width: 9px; height: 9px; background: #111; display: block; }
  .hero-dots span.active { background: var(--red); }

  /* Welcome */
  .section-title { color: var(--red); font-weight: 700; }
  .welcome-title { left: 74px; top: 436px; font-size: 17px; }
  .welcome-text { left: 74px; top: 462px; width: 314px; font-size: 9.3px; line-height: 11.8px; color: var(--muted); text-align: justify; }
  .welcome-text p + p { margin-top: 8px; }
  .welcome-photo { left: 406px; top: 448px; width: 261px; height: 158px; background: linear-gradient(90deg, #d7dde4 0%, #a9b8c8 50%, #6f87a3 100%); }

  /* News */
  .news-title { left: 74px; top: 631px; font-size: 12px; }
  .btn-more { height: 15px; background: var(--red); color: var(--white); font-size: 7.5px; text-align: center; line-height: 15px; border-radius: 2px; }
  .news-item { top: 662px; width: 190px; }
  .date-circle { position: absolute; left: 0; top: 2px; width: 42px; height: 42px; border-radius: 50%; background: #ececec; font-size: 10.5px; text-align: center; line-height: 12.5px; padding-top: 8px; color: #222; }
  .news-heading { position: absolute; left: 52px; top: 0; font-size: 11px; white-space: nowrap; }
  .news-text { position: absolute; left: 53px; top: 20px; width: 137px; font-size: 7.5px; line-height: 9.6px; color: var(--muted); }

  .divider { left: 468px; top: 618px; width: 1px; height: 342px; background: #e2e2e2; }

  /* Events */
  .events-title { left: 75px; top: 754px; font-size: 12px; }
  .event-heading { font-size: 8.2px; color: #222; white-space: nowrap; }
  .date-box { width: 24px; height: 26px; background: #ececec; font-size: 8px; text-align: center; line-height: 9.5px; padding-top: 3px; color: #222; }
  .event-text { width: 230px; font-size: 7.5px; line-height: 9.6px; color: var(--muted); }
  .event-photo-water { left: 352px; top: 768px; width: 92px; height: 76px; background: linear-gradient(180deg, #f2f7fb 0%, #bcd8ea 100%); }
  .event-photo-road { left: 79px; top: 854px; width: 92px; height: 76px; background: linear-gradient(180deg, #8da0b3 0%, #5d6670 60%, #3c3f44 100%); }

  /* Contact */
  .contact-title { left: 474px; top: 624px; font-size: 12px; }
  .contact-intro { left: 474px; top: 650px; font-size: 8px; color: #666; line-height: 20.8px; }
  .field { left: 474px; width: 168px; height: 19px; background: var(--field); font-size: 8px; color: #888; padding: 5px 0 0 8px; border-radius: 2px; }
  .btn-submit { left: 530px; top: 792px; width: 55px; height: 15px; background: var(--red); color: var(--white); font-size: 8px; text-align: center; line-height: 15px; border-radius: 2px; }
  .contact-alt { left: 482px; top: 822px; font-size: 8px; color: #222; line-height: 16.8px; }
  .contact-line { left: 483px; font-size: 8px; color: #222; display: flex; align-items: center; gap: 6px; }
  .contact-or { left: 483px; top: 902px; font-size: 8px; color: #222; }
  .btn-site { left: 501px; top: 900px; width: 106px; height: 15px; background: var(--red); color: var(--white); font-size: 7.5px; text-align: center; line-height: 15px; border-radius: 3px; }

  /* Newsletter */
  .newsletter { left: 0; top: 972px; width: 739px; height: 54px; background: var(--band); }
  .newsletter-title { left: 112px; top: 12px; font-size: 12px; color: #111; }
  .newsletter-sub { left: 187px; top: 29px; font-size: 8px; color: #111; }
  .nl-input { top: 13px; width: 108px; height: 21px; background: var(--white); font-size: 7.5px; color: #999; padding: 7px 0 0 9px; }
  .btn-signin-now { left: 537px; top: 13px; width: 96px; height: 21px; background: linear-gradient(var(--red), var(--red-dark)); color: var(--white); font-size: 10.5px; text-align: center; line-height: 21px; border-radius: 3px; }

  /* Footer */
  .site-footer { left: 0; top: 1026px; width: 739px; height: 146px; background: linear-gradient(var(--red), var(--red-deep)); color: var(--white); }
  .footer-heading { top: 13px; font-size: 12px; }
  .footer-links { top: 44px; list-style: none; font-size: 8px; line-height: 14.8px; }
  .tweet-icon { left: 346px; top: 38px; width: 20px; height: 20px; border-radius: 50%; background: #29a9d8; }
  .tweet-text { left: 354px; top: 38px; width: 145px; font-size: 7.2px; line-height: 9.6px; text-indent: 18px; }
  .tweet-meta { left: 353px; top: 100px; font-size: 7px; }
  .footer-contact { left: 524px; top: 40px; font-size: 8px; line-height: 12.5px; }
  .footer-contact .line { display: flex; align-items: center; gap: 8px; }
  .footer-bottom { left: 0; top: 1172px; width: 739px; height: 28px; background: var(--red-dark); color: var(--white); font-size: 7.5px; }
  .copyright { left: 304px; top: 9px; }
  .page-code { left: 626px; top: 9px; }
</style>
</head>
<body>

<header class="site-header">
  <div class="abs brand"><span class="brand-mark"></span><span class="brand-name">VANGRIDEX</span></div>
  <div class="abs social" aria-label="Social links"><span></span><span></span><span></span><span></span></div>
  <div class="abs call">Call : 1800 640 317</div>
  <div class="abs btn-signin">Signin</div>
  <div class="abs btn-register">Register</div>
</header>

<nav class="abs main-nav">
  <a style="left:81px">Home</a>
  <a style="left:130px">Business Units</a>
  <a style="left:218px">Services</a>
  <a style="left:276px">About Us</a>
  <a style="left:340px">Locations</a>
  <a style="left:406px">Contact Us</a>
  <div class="abs search">Search
    <svg width="14" height="14" viewBox="0 0 14 14"><circle cx="6" cy="6" r="4.5" fill="none" stroke="#777" stroke-width="1.4"/><line x1="9.3" y1="9.3" x2="13" y2="13" stroke="#777" stroke-width="1.6"/></svg>
  </div>
</nav>

<section class="abs hero" role="img" aria-label="Passenger jet taking off against a cloudy sunset sky">
  <div class="abs hero-caption">We work in Systems and Technology space for Transportation, Government and Commercial sectors</div>
  <div class="abs hero-dots"><span></span><span></span><span></span><span class="active"></span></div>
</section>

<section>
  <h1 class="abs section-title welcome-title">Welcome</h1>
  <div class="abs welcome-text">
    <p>We have the expertise to deliver the exclusive system. And technical quality. To support and accommodate larger business goals. Our management system is a tool that supports the model and business needs. We understand that the most technical concepts that support the vision of a true business goals</p>
    <p>We will take steps to ensure that the knowledge and expertise of our. Be in the professional services we deliver to our customers to achieve such goals. , we believe that the Zone East and Asia. A market that is growing the economy and projects. Developed infrastructure Which requires management systems and specialized.</p>
  </div>
  <div class="abs welcome-photo" role="img" aria-label="Smiling businesswoman in front of a blurred team of colleagues"></div>
</section>

<section>
  <h2 class="abs section-title news-title">Latest News</h2>
  <div class="abs btn-more" style="left:372px;top:631px;width:79px">See more News &nbsp;❯</div>
  <article class="abs news-item" style="left:73px">
    <div class="date-circle">27<br>Feb</div>
    <h3 class="news-heading" style="font-weight:400">What About The Vangridex?</h3>
    <p class="news-text">Lorem ipsum dolor sit amet, consecte-tur adipisicing elit, sed do eiusmod tempor incididunt ut labore et dolore magna aliqua.</p>
  </article>
  <article class="abs news-item" style="left:269px">
    <div class="date-circle">27<br>Feb</div>
    <h3 class="news-heading" style="font-weight:400">What About The Vangridex?</h3>
    <p class="news-text">Lorem ipsum dolor sit amet, consecte-tur adipisicing elit, sed do eiusmod tempor incididunt ut labore et dolore magna aliqua.</p>
  </article>
</section>

<div class="abs divider"></div>

<section>
  <h2 class="abs section-title events-title">Events</h2>
  <div class="abs event-heading" style="left:76px;top:776px">About New Events : Every month blogging a Events</div>
  <div class="abs date-box" style="left:74px;top:803px">27<br>Feb</div>
  <p class="abs event-text" style="left:109px;top:794px">Lorem ipsum dolor sit amet, consectetur adipisicing elit, sed do eius-mod tempor incididunt ut labore et dolore magna aliqua. Ut enim ad minim veniam, quis nostrud exercitation ullamco</p>
  <div class="abs event-photo-water" role="img" aria-label="Goldfish leaping between two glass bowls of water"></div>

  <div class="abs event-photo-road" role="img" aria-label="Truck speeding along a highway"></div>
  <div class="abs event-heading" style="left:193px;top:863px">About New Events : Every month blogging a Events</div>
  <div class="abs date-box" style="left:190px;top:890px">27<br>Feb</div>
  <p class="abs event-text" style="left:226px;top:881px">Lorem ipsum dolor sit amet, consectetur adipisicing elit, sed do eius-mod tempor incididunt ut labore et dolore magna aliqua. Ut enim ad minim veniam, quis nostrud exercitation ullamco</p>
  <div class="abs btn-more" style="left:378px;top:934px;width:78px">See more Events &nbsp;❯</div>
</section>

<aside>
  <h2 class="abs section-title contact-title">Contact Us</h2>
  <div class="abs contact-intro">If you have questions or want to know more?<br>We are happy to contact you:</div>
  <div class="abs field" style="top:692px">Name</div>
  <div class="abs field" style="top:717px">Telephone Number</div>
  <div class="abs field" style="top:742px">Email</div>
  <div class="abs field" style="top:767px">Message</div>
  <div class="abs btn-submit">Submit</div>
  <div class="abs contact-alt">Would you rather do us?<br>You can us reached through</div>
  <div class="abs contact-line" style="top:864px">
    <svg width="9" height="9" viewBox="0 0 10 10"><path d="M2 1 L4 1 L5 3.5 L3.8 4.5 Q4.8 6.2 5.5 6.2 L6.5 5 L9 6 L9 8 Q8 9.2 6.5 9 Q1.5 7 1 2.5 Q1 1.3 2 1Z" fill="#222"/></svg>1800 - 5678</div>
  <div class="abs contact-line" style="top:877px">
    <svg width="10" height="9" viewBox="0 0 10 9"><rect x="0.6" y="1.6" width="8.8" height="6.8" fill="none" stroke="#222" stroke-width="1.2"/><path d="M0.6 1.6 L5 5.4 L9.4 1.6" fill="none" stroke="#222" stroke-width="1.2"/></svg>info@sitename.com</div>
  <div class="abs contact-or">Or</div>
  <div class="abs btn-site">contact us via the site »</div>
</aside>

<section class="abs newsletter">
  <div class="abs newsletter-title">To stay on top of your Vangridex?</div>
  <div class="abs newsletter-sub">Subscribe to our newsletter</div>
  <div class="abs nl-input" style="left:313px">Name</div>
  <div class="abs nl-input" style="left:425px">Email</div>
  <div class="abs btn-signin-now">Sign in Now</div>
</section>

<footer class="abs site-footer">
  <h3 class="abs footer-heading" style="left:106px;font-weight:400">Quick Links</h3>
  <ul class="abs footer-links" style="left:108px">
    <li>Home</li><li>Business Units</li><li>Services</li><li>About Us</li><li>Locations</li><li>Contact Us</li>
  </ul>
  <h3 class="abs footer-heading" style="left:218px;font-weight:400">Interesting links</h3>
  <ul class="abs footer-links" style="left:221px">
    <li>Terms &amp; Conditions</li><li>Disclaimer</li><li>Privacy Policy</li>
  </ul>
  <h3 class="abs footer-heading" style="left:350px;font-weight:400">Chirpline</h3>
  <div class="abs tweet-icon"></div>
  <p class="abs tweet-text">&nbsp;&nbsp;&nbsp;Lorem ipsum dolor sit amet, consectetur ad pisci elit. In tempor, velit sheet ornare auctor, Arcu lor em volutpat diam, sed bibendum magna risus ut tortor. Pellentesque a risus.</p>
  <div class="abs tweet-meta">@ sitename - 31 Aug 2013 - 10:26</div>
  <h3 class="abs footer-heading" style="left:521px;font-weight:400">Contact</h3>
  <div class="abs footer-contact">
    <div>Vangridex Ltd.,</div>
    <div style="height:12px"></div>
    <div class="line"><svg width="9" height="9" viewBox="0 0 10 10"><path d="M2 1 L4 1 L5 3.5 L3.8 4.5 Q4.8 6.2 5.5 6.2 L6.5 5 L9 6 L9 8 Q8 9.2 6.5 9 Q1.5 7 1 2.5 Q1 1.3 2 1Z" fill="#fff"/></svg>&nbsp;1800 - 5678</div>
    <div class="line"><svg width="10" height="9" viewBox="0 0 10 9"><rect x="0.6" y="1.6" width="8.8" height="6.8" fill="none" stroke="#fff" stroke-width="1.2"/><path d="M0.6 1.6 L5 5.4 L9.4 1.6" fill="none" stroke="#fff" stroke-width="1.2"/></svg>info@sitename.com</div>
  </div>
</footer>

<div class="abs footer-bottom">
  <div class="abs copyright">© 2014.www.companyname.com</div>
  <div class="abs page-code">M1</div>
</div>

</body>
</html>
```